Webdesign für Branchenverzeichnis
Zielgruppe
Wir-bauen-Brücken – das Branchenverzeichnis der Selbstverantwortlichen.
Der Anbieter präsentiert sich mit seinem Namen und der URL - ähnlich wie bei 'blaue Blätter' oder Torkwerk.
Aufgabenstellung
Das Branchenverzeichnis sollte neutral und gleichzeitig hochwertig sein. Die Hauptfarben sind Gold, Schwarz und Weiß. Logo und Corporate Design wurden bereits entwickelt

```html
<!DOCTYPE html>
<html lang="de">
<head>
<meta charset="utf-8">
<title>Wir-bauen-Brücken – Suchen</title>
<link href="https://fonts.googleapis.com/css2?family=Quicksand:wght@400;500;600;700&display=swap" rel="stylesheet">
<style>
:root{
  --gold:#d5b26c;
  --gold-dark:#c9a55d;
  --ink:#1c1c1c;
  --grey:#6d6d6d;
  --btn:#3b3b3b;
  --card:#fbf8ea;
  --card-line:#ece3c3;
  --page:#fbfbfa;
  --white:#ffffff;
}
*{box-sizing:border-box;margin:0;padding:0}
html,body{width:1025px;height:1200px;overflow:hidden}
body{position:relative;background:var(--page);font-family:'Quicksand',sans-serif;color:var(--ink)}
.abs{position:absolute}

/* Header */
.site-header{position:absolute;left:0;top:0;width:1025px;height:53px;background:linear-gradient(#2f2f2f,#5a5a5a);}
.brand{position:absolute;left:118px;top:19px;font-size:10px;font-weight:600;color:var(--gold);letter-spacing:.3px}
.nav a{position:absolute;top:22px;font-size:7.5px;font-weight:600;letter-spacing:1.1px;color:var(--white);text-decoration:none;transform:translateX(-50%)}
.nav a.active{color:var(--gold)}
.icon-box{position:absolute;top:16px;width:21px;height:21px;border:1px solid var(--gold);display:flex;align-items:center;justify-content:center}
.cta{position:absolute;left:785px;top:15px;width:106px;height:23px;background:var(--gold);color:var(--white);font-size:6.5px;font-weight:600;letter-spacing:.8px;display:flex;align-items:center;justify-content:center}

/* Hero */
.hero-title{position:absolute;left:0;width:512px;top:81px;text-align:center;font-size:19px;font-weight:600;letter-spacing:2.6px}
.hero-title span{color:var(--gold)}
.hero-sub{position:absolute;left:0;width:512px;top:114px;text-align:center;font-size:8.5px;letter-spacing:.9px;color:#333}

/* Search band */
.search-band{position:absolute;left:0;top:154px;width:512px;height:61px;background:var(--gold);box-shadow:0 4px 8px rgba(0,0,0,.12)}
.field{position:absolute;top:17px;width:117px;height:26px;background:var(--white);font-size:6.5px;color:#777;display:flex;align-items:center;padding-left:11px}
.field svg{position:absolute;right:10px}
.search-btn{position:absolute;left:403px;top:17px;width:80px;height:27px;background:var(--btn);color:var(--white);font-size:7px;font-weight:600;letter-spacing:.8px;display:flex;align-items:center;justify-content:center}

/* Results */
.results-title{position:absolute;left:30px;top:232px;font-size:11px;letter-spacing:.3px}
.results-title span{color:var(--gold)}
.results-count{position:absolute;left:30px;top:251px;font-size:7.5px;color:var(--grey);letter-spacing:.4px}
.sort-label{position:absolute;left:333px;top:251px;font-size:7.5px;color:var(--grey);letter-spacing:.4px}
.sort-select{position:absolute;left:401px;top:246px;width:82px;height:19px;border:1px solid #ddd;background:var(--white);font-size:5.8px;color:#888;padding-left:8px;display:flex;align-items:center}
.sort-select svg{position:absolute;right:6px}
.rule{position:absolute;left:30px;top:271px;width:453px;height:1px;background:#d5d5d5}

.card{position:absolute;left:30px;width:453px;height:106px;background:var(--card);border:1px solid var(--card-line)}
.card-photo{position:absolute;left:0;top:0;width:111px;height:104px;background:linear-gradient(135deg,#c9c2b6,#6b6258 55%,#8a6a4a)}
.card-name{position:absolute;left:122px;top:10px;font-size:12px;font-weight:500;letter-spacing:.5px}
.card-meta{position:absolute;top:29px;font-size:6.3px;color:#444;letter-spacing:.3px;display:flex;align-items:center;gap:3px}
.card-text{position:absolute;left:120px;top:52px;width:322px;font-size:6.6px;line-height:10px;color:#7a7a7a}
.card-btn{position:absolute;left:372px;top:11px;width:67px;height:21px;background:var(--btn);color:var(--white);font-size:6.3px;letter-spacing:.6px;display:flex;align-items:center;justify-content:center}

.pager{position:absolute;top:921px;width:27px;height:27px;border:1px solid var(--gold);font-size:10px;color:#555;display:flex;align-items:center;justify-content:center;background:var(--white)}
.pager.current{color:var(--gold);font-weight:700}

/* Map */
.map{position:absolute;left:512px;top:53px;width:513px;height:916px;background:linear-gradient(160deg,#e9e4da 0%,#ece6dc 45%,#cfe0e6 70%,#aed3df 100%)}

/* Footer */
.site-footer{position:absolute;left:0;top:969px;width:1025px;height:231px;background:linear-gradient(#5b5b5b,#2e2e2e)}
.footer-brand{position:absolute;left:214px;top:75px;width:62px;font-size:9px;font-weight:600;color:var(--white);line-height:12px;text-align:center}
.footer-title{position:absolute;top:68px;font-size:10px;font-weight:700;color:var(--white);letter-spacing:.4px}
.footer-about{position:absolute;left:307px;top:90px;width:165px;font-size:8px;line-height:13.4px;color:#e8e8e8}
.footer-about a{color:var(--gold);display:block;margin-top:3px}
.footer-col a{position:absolute;font-size:8px;color:#e8e8e8;text-decoration:none}
.copyright{position:absolute;left:0;width:1025px;top:207px;text-align:center;font-size:6.5px;font-weight:600;color:var(--white)}
</style>
</head>
<body>

<header class="site-header">
  <div class="brand">Wir-bauen-Brücken</div>
  <nav class="nav">
    <a style="left:258px">HOME</a>
    <a class="active" style="left:327px">SUCHEN</a>
    <a style="left:406px">ÜBER UNS</a>
    <a style="left:503px">MITGLIEDSCHAFT</a>
    <a style="left:597px">KONTAKT</a>
  </nav>
  <div class="icon-box" style="left:704px">
    <svg width="15" height="10"><rect width="15" height="3.4" fill="#000"/><rect y="3.3" width="15" height="3.4" fill="#d00"/><rect y="6.6" width="15" height="3.4" fill="#fc0"/></svg>
  </div>
  <div class="icon-box" style="left:732px">
    <svg width="11" height="11" viewBox="0 0 11 11"><circle cx="5.5" cy="3.3" r="2.5" fill="#d5b26c"/><path d="M1 11c0-3 2-4.5 4.5-4.5S10 8 10 11z" fill="#d5b26c"/></svg>
  </div>
  <div class="cta">MITGLIED WERDEN</div>
</header>

<h1 class="hero-title">WIR ZEIGEN <span>UNTERNEHMER</span></h1>
<p class="hero-sub">Suche in deiner Region und finde neue Unternehmen in vielen Branchen &amp; Ländern.</p>

<section class="search-band">
  <div class="field" style="left:30px">Unternehmen, Name
    <svg width="15" height="13" viewBox="0 0 15 13"><path d="M7.5 0L0 6.5h2V13h4V9h3v4h4V6.5h2z" fill="#d5b26c"/></svg>
  </div>
  <div class="field" style="left:152px">Stadt, PLZ oder Land
    <svg width="15" height="15" viewBox="0 0 15 15"><circle cx="7.5" cy="7.5" r="5" fill="none" stroke="#d5b26c" stroke-width="1.3"/><circle cx="7.5" cy="7.5" r="2" fill="#d5b26c"/><path d="M7.5 0v2.5M7.5 12.5V15M0 7.5h2.5M12.5 7.5H15" stroke="#d5b26c" stroke-width="1.3"/></svg>
  </div>
  <div class="field" style="left:275px">IT &amp; Marketing
    <svg width="11" height="7" viewBox="0 0 11 7"><path d="M1 1l4.5 4.5L10 1" fill="none" stroke="#d5b26c" stroke-width="1.5"/></svg>
  </div>
  <div class="search-btn">SUCHEN</div>
</section>

<h2 class="results-title" style="font-weight:500">Ihre Suchergebnisse für: <span>IT &amp; Marketing</span></h2>
<p class="results-count">Zeige 5 von 25 Brancheneinträgen</p>
<p class="sort-label">Sortieren nach</p>
<div class="sort-select">Firmenname A-Z
  <svg width="8" height="5" viewBox="0 0 8 5"><path d="M1 1l3 3 3-3" fill="none" stroke="#d5b26c" stroke-width="1.2"/></svg>
</div>
<div class="rule"></div>

<article class="card" style="top:296px">
  <div class="card-photo" role="img" aria-label="Foto: zwei Personen im Besprechungsraum"></div>
  <h3 class="card-name">Firmenname</h3>
  <div class="card-meta" style="left:122px"><svg width="7" height="7"><rect x=".5" y="1" width="6" height="5.5" fill="none" stroke="#d5b26c"/></svg>IT &amp; Marketing</div>
  <div class="card-meta" style="left:205px"><svg width="6" height="8" viewBox="0 0 6 8"><path d="M3 0a3 3 0 0 0-3 3c0 2 3 5 3 5s3-3 3-5a3 3 0 0 0-3-3z" fill="#d5b26c"/></svg>München</div>
  <p class="card-text">Lorem ipsum dolor sit amet, consectetur adipisicing elit, sed do eiusmod tempor incididunt ut labore et dolore, magna aliqua. Duis aute irure dolor in reprehenderit in voluptate velit esse ci dolore eu fugiat nulla pariatur. Ut enim ad minim veniam, quis nostrud exercitation ullamco la nisi ut aliquip ex ea commodo!</p>
  <div class="card-btn">ZUR WEBSITE</div>
</article>

<article class="card" style="top:419px">
  <div class="card-photo" role="img" aria-label="Foto: zwei Personen im Besprechungsraum"></div>
  <h3 class="card-name">Firmenname</h3>
  <div class="card-meta" style="left:122px"><svg width="7" height="7"><rect x=".5" y="1" width="6" height="5.5" fill="none" stroke="#d5b26c"/></svg>IT &amp; Marketing</div>
  <div class="card-meta" style="left:205px"><svg width="6" height="8" viewBox="0 0 6 8"><path d="M3 0a3 3 0 0 0-3 3c0 2 3 5 3 5s3-3 3-5a3 3 0 0 0-3-3z" fill="#d5b26c"/></svg>München</div>
  <p class="card-text">Lorem ipsum dolor sit amet, consectetur adipisicing elit, sed do eiusmod tempor incididunt ut labore et dolore, magna aliqua. Duis aute irure dolor in reprehenderit in voluptate velit esse ci dolore eu fugiat nulla pariatur. Ut enim ad minim veniam, quis nostrud exercitation ullamco la nisi ut aliquip ex ea commodo!</p>
  <div class="card-btn">ZUR WEBSITE</div>
</article>

<article class="card" style="top:540px">
  <div class="card-photo" role="img" aria-label="Foto: zwei Personen im Besprechungsraum"></div>
  <h3 class="card-name">Firmenname</h3>
  <div class="card-meta" style="left:122px"><svg width="7" height="7"><rect x=".5" y="1" width="6" height="5.5" fill="none" stroke="#d5b26c"/></svg>IT &amp; Marketing</div>
  <div class="card-meta" style="left:205px"><svg width="6" height="8" viewBox="0 0 6 8"><path d="M3 0a3 3 0 0 0-3 3c0 2 3 5 3 5s3-3 3-5a3 3 0 0 0-3-3z" fill="#d5b26c"/></svg>München</div>
  <p class="card-text">Lorem ipsum dolor sit amet, consectetur adipisicing elit, sed do eiusmod tempor incididunt ut labore et dolore, magna aliqua. Duis aute irure dolor in reprehenderit in voluptate velit esse ci dolore eu fugiat nulla pariatur. Ut enim ad minim veniam, quis nostrud exercitation ullamco la nisi ut aliquip ex ea commodo!</p>
  <div class="card-btn">ZUR WEBSITE</div>
</article>

<article class="card" style="top:659px">
  <div class="card-photo" role="img" aria-label="Foto: zwei Personen im Besprechungsraum"></div>
  <h3 class="card-name">Firmenname</h3>
  <div class="card-meta" style="left:122px"><svg width="7" height="7"><rect x=".5" y="1" width="6" height="5.5" fill="none" stroke="#d5b26c"/></svg>IT &amp; Marketing</div>
  <div class="card-meta" style="left:205px"><svg width="6" height="8" viewBox="0 0 6 8"><path d="M3 0a3 3 0 0 0-3 3c0 2 3 5 3 5s3-3 3-5a3 3 0 0 0-3-3z" fill="#d5b26c"/></svg>München</div>
  <p class="card-text">Lorem ipsum dolor sit amet, consectetur adipisicing elit, sed do eiusmod tempor incididunt ut labore et dolore, magna aliqua. Duis aute irure dolor in reprehenderit in voluptate velit esse ci dolore eu fugiat nulla pariatur. Ut enim ad minim veniam, quis nostrud exercitation ullamco la nisi ut aliquip ex ea commodo!</p>
  <div class="card-btn">ZUR WEBSITE</div>
</article>

<article class="card" style="top:780px">
  <div class="card-photo" role="img" aria-label="Foto: zwei Personen im Besprechungsraum"></div>
  <h3 class="card-name">Firmenname</h3>
  <div class="card-meta" style="left:122px"><svg width="7" height="7"><rect x=".5" y="1" width="6" height="5.5" fill="none" stroke="#d5b26c"/></svg>IT &amp; Marketing</div>
  <div class="card-meta" style="left:205px"><svg width="6" height="8" viewBox="0 0 6 8"><path d="M3 0a3 3 0 0 0-3 3c0 2 3 5 3 5s3-3 3-5a3 3 0 0 0-3-3z" fill="#d5b26c"/></svg>München</div>
  <p class="card-text">Lorem ipsum dolor sit amet, consectetur adipisicing elit, sed do eiusmod tempor incididunt ut labore et dolore, magna aliqua. Duis aute irure dolor in reprehenderit in voluptate velit esse ci dolore eu fugiat nulla pariatur. Ut enim ad minim veniam, quis nostrud exercitation ullamco la nisi ut aliquip ex ea commodo!</p>
  <div class="card-btn">ZUR WEBSITE</div>
</article>

<div class="pager current" style="left:179px">1</div>
<div class="pager" style="left:211px">2</div>
<div class="pager" style="left:243px">3</div>
<div class="pager" style="left:275px">4</div>
<div class="pager" style="left:307px">5</div>

<div class="map" role="img" aria-label="Stadtkarte mit Standortmarkierungen der Unternehmen"></div>

<footer class="site-footer">
  <div class="footer-brand">Wir-bauen-Brücken</div>
  <h4 class="footer-title" style="left:307px">Wir bauen Brücken</h4>
  <p class="footer-about">Duis sed odio sit amet nibh vulputate cursus a sit amet mauris. Morbi accumsan ipsum velit. Nam nec tellus a <a>Über uns</a></p>

  <h4 class="footer-title" style="left:553px;top:66px">WEBSITE</h4>
  <div class="footer-col">
    <a style="left:553px;top:91px">Wir bauen Brücken</a>
    <a style="left:553px;top:112px">Unternehmen suchen</a>
    <a style="left:553px;top:134px">Mitgliedschaft</a>
    <a style="left:553px;top:155px">Kontakt</a>
  </div>

  <h4 class="footer-title" style="left:716px;top:66px">RECHTLICHES</h4>
  <div class="footer-col">
    <a style="left:716px;top:91px">Impressum</a>
    <a style="left:716px;top:112px">Datenschutz</a>
    <a style="left:716px;top:134px">AGB</a>
    <a style="left:716px;top:155px">Sicherheitsbestimmungen</a>
  </div>

  <p class="copyright">© 2020 Wir bauen Brücken</p>
</footer>

</body>
</html>
```